Email Preference Page Design

We are looking for a 2 page design for our users to edit their email preferences and submit friend referrals. You can find the fuctionality, content and text here:

https://brightreel.mailvector.example/app/linkClick/7281/5b9c1d04e6a7f318/20583147/8d4f2a61c0b9e357

* the shipping and billing address might be different so you need to show the billing if the "same as shipping" box is not checked. It can auto-hide like the page above shows if that fits your design.

* when the "unsubscribe from all email lists" box is selected, all the other checkbox options will hide as in the example page. We need you to show us what the site will look like with and without that checkbox selected.

We want to match these two pages to the general feel of these website pages:

www.brightreel.example
and
free.brightreel.example

The page should be very clean and tight. Project is for design only but must be able to be implemented in html showing button and checkbox states. Technically this must be two pages for our system - one for all the user info and one for individual email referrals (see example above).

Target Market(s)

video professionals

Industry/Entity Type

Shipping

Requirements
Must have
• our logo (see numerous versions attached)
well designed header
well designed sections
clean editable text
tight layout
html friendly
easy to understand
2 pages
Nice to have
• custom checkboxes and radio buttons

```html
<!DOCTYPE html>
<html lang="en">
<head>
<meta charset="utf-8">
<title>BrightReel – Communication Preferences</title>
<link rel="stylesheet" href="https://fonts.googleapis.com/css2?family=Oswald:wght@300;400;500&family=Open+Sans:wght@400;600&display=swap">
<style>
  :root{
    --stage:#a7a7a7;
    --page:#ffffff;
    --navy:#1d2f3f;
    --ink:#1b1b1b;
    --orange:#e8590c;
    --orange-soft:#f08a3c;
    --gold:#f2a41c;
    --yellow:#fde15c;
    --yellow-edge:#f3d04a;
    --lime:#e7ea8e;
    --blue:#2b9fd6;
    --grey:#6d6d6d;
    --rule:#ef8a4a;
    --field-border:#3a3a3a;
  }
  *{box-sizing:border-box;margin:0;padding:0}
  html,body{width:1091px;height:1200px;overflow:hidden}
  body{background:var(--stage);font-family:"Oswald",sans-serif;font-weight:300;color:var(--ink)}

  .page{position:absolute;left:123px;top:0;width:844px;height:1200px;background:var(--page);overflow:hidden}

  /* header */
  .site-header{position:absolute;left:0;top:0;width:100%;height:75px;border-bottom:1px dashed #d6d6d6}
  .brand{position:absolute;left:119px;top:14px;display:flex;align-items:center;gap:10px}
  .brand-dot{width:26px;height:26px;border-radius:50%;background:var(--gold)}
  .brand-name{font-family:"Oswald",sans-serif;font-weight:400;font-size:36px;line-height:44px;color:var(--navy);letter-spacing:.5px}
  .page-title{position:absolute;left:458px;top:20px;font-weight:400;font-size:25px;line-height:32px;color:var(--gold)}

  .hero{position:absolute;left:0;top:75px;width:100%;height:183px;
    background:linear-gradient(100deg,#5a3a22 0%,#b36b2c 22%,#7a4a25 45%,#d08a3a 60%,#6a4426 80%,#8a5a30 100%)}

  /* contact card */
  .contact-card{position:absolute;left:91px;top:200px;width:648px;height:295px;background:var(--yellow);border-radius:6px;border:1px solid var(--yellow-edge)}
  .section-title{font-weight:400;font-size:21px;color:var(--orange);line-height:26px}
  .contact-card .section-title{position:absolute;left:33px;top:18px}
  .field-col{position:absolute;top:57px;display:flex;flex-direction:column;gap:8px}
  .field-col.left{left:0}
  .field-col.right{left:300px}
  .field{display:flex;align-items:center;height:24px}
  .field label{font-size:14px;text-align:right;padding-right:7px;white-space:nowrap}
  .field-col.left label{width:94px}
  .field-col.right label{width:94px}
  .req{color:var(--orange)}
  .input{height:24px;width:208px;background:#fff;border:1.5px solid var(--field-border);border-radius:4px;box-shadow:inset 0 2px 2px rgba(0,0,0,.18)}
  .select{display:flex;align-items:center;justify-content:space-between;padding:0 8px;font-size:12px;background:linear-gradient(#fafafa,#d9d9d9);box-shadow:none}
  .postal{display:flex;gap:12px}
  .postal .zip{width:114px}
  .postal .ext{width:82px}

  .subscribe{position:absolute;left:387px;top:209px;display:flex;gap:7px;font-size:14px;line-height:15px}
  .subscribe small{display:block;font-size:12px;line-height:14px;color:#333;margin-top:1px}

  /* checkboxes */
  .box{flex:none;width:15px;height:15px;border:1.5px solid var(--orange-soft);border-radius:3px;background:#fff;display:inline-flex;align-items:center;justify-content:center}
  .box svg{width:11px;height:11px;display:none}
  .box.checked svg{display:block}
  .box.ink{border-color:#222}
  .box.blue{border-color:var(--blue)}
  .box.grey{border-color:var(--grey)}
  .box path{fill:none;stroke-width:2.4;stroke-linecap:round;stroke-linejoin:round}
  .box path{stroke:var(--orange)}
  .box.blue path{stroke:var(--blue)}
  .box.grey path{stroke:#444}

  /* shipping */
  .shipping-bar{position:absolute;left:91px;top:508px;width:648px;height:62px;background:var(--lime);border-radius:6px;border-top:1px dashed #fff;display:flex;align-items:center;padding-left:33px}
  .shipping-bar .option{margin-left:40px;display:flex;align-items:center;gap:7px;font-size:14px}

  /* filter */
  .filter{position:absolute;left:124px;top:596px;width:616px}
  .filter-sub{font-weight:400;font-size:13px;color:var(--orange);margin-top:1px}
  .rule{height:1px;background:var(--rule);margin-top:14px}
  .choices{display:flex;margin-top:13px}
  .choice-col{width:338px}
  .choice-col h3{font-weight:300;font-size:16px;line-height:22px;margin-bottom:6px}
  .choice-col ul{list-style:none}
  .choice-col li{display:flex;align-items:center;gap:8px;height:26.3px;font-size:14px}
  .extras{position:absolute;left:443px;top:907px;width:296px;height:73px;border:1px solid #888;border-radius:8px;padding:11px 0 0 19px}
  .extras li{list-style:none;display:flex;align-items:center;gap:8px;height:26px;font-size:14px;color:#555}
  .rule.bottom{position:absolute;left:124px;top:999px;width:616px;margin:0}

  .submit{position:absolute;left:124px;top:1016px;width:186px;height:44px;border-radius:22px;background:var(--orange);color:#fff;font-family:"Oswald",sans-serif;font-weight:400;font-size:21px;border:none;display:flex;align-items:center;justify-content:center;gap:14px}
  .submit svg{width:24px;height:24px}

  /* footer */
  .site-footer{position:absolute;left:0;top:1110px;width:100%;height:90px;background:var(--navy);text-align:center;border-top:1px solid #eee}
  .site-footer p{font-family:"Open Sans",sans-serif;font-weight:600;font-size:10px;color:#fff;margin-top:22px}
  .social{display:flex;justify-content:center;gap:6px;margin-top:16px}
  .social span{width:23px;height:23px;border-radius:50%;border:1.5px solid var(--gold)}
</style>
</head>
<body>
<div class="page">
  <header class="site-header">
    <div class="brand"><span class="brand-dot"></span><span class="brand-name">brightreel</span></div>
    <h1 class="page-title">Communication Preferences</h1>
  </header>

  <div class="hero" role="img" aria-label="Blurred night city street with streaking lights and taxis"></div>

  <section class="contact-card">
    <h2 class="section-title">Contact info</h2>
    <div class="field-col left">
      <div class="field"><label>First Name <span class="req">*</span></label><span class="input"></span></div>
      <div class="field"><label>Last Name <span class="req">*</span></label><span class="input"></span></div>
      <div class="field"><label>Email <span class="req">*</span></label><span class="input"></span></div>
      <div class="field"><label>Phone</label><span class="input"></span></div>
      <div class="field"><label>Address 1</label><span class="input"></span></div>
      <div class="field"><label>Address 2</label><span class="input"></span></div>
      <div class="field"><label>Address 3</label><span class="input"></span></div>
    </div>
    <div class="field-col right">
      <div class="field"><label>City</label><span class="input"></span></div>
      <div class="field"><label>Country</label><span class="input select">United States of America
        <svg width="10" height="8" viewBox="0 0 10 8"><path d="M0 0h10L5 8z" fill="#111"/></svg></span></div>
      <div class="field"><label>State</label><span class="input"></span></div>
      <div class="field"><label>Postal Code</label><span class="postal"><span class="input zip"></span><span class="input ext"></span></span></div>
    </div>
    <div class="subscribe">
      <span class="box ink"><svg viewBox="0 0 12 12"><path d="M2 6.5l2.7 2.7L10 3"/></svg></span>
      <div>Subscribe me to your general email list
        <small>This monthly email includes free video loops<br>and VIP sale notices.</small></div>
    </div>
  </section>

  <section class="shipping-bar">
    <h2 class="section-title">Shipping address</h2>
    <div class="option"><span class="box ink checked"><svg viewBox="0 0 12 12"><path d="M2 6.5l2.7 2.7L10 3"/></svg></span>Billing address is same as shipping address</div>
  </section>

  <section class="filter">
    <h2 class="section-title">Filter email</h2>
    <p class="filter-sub">Help us filter our emails, so we are only sending relevant informations to you</p>
    <div class="rule"></div>
    <div class="choices">
      <div class="choice-col">
        <h3>Send me emails about these product types</h3>
        <ul>
          <li><span class="box checked"><svg viewBox="0 0 12 12"><path d="M2 6.5l2.7 2.7L10 3"/></svg></span>Low energy motion loops</li>
          <li><span class="box checked"><svg viewBox="0 0 12 12"><path d="M2 6.5l2.7 2.7L10 3"/></svg></span>High energy motion loops</li>
          <li><span class="box checked"><svg viewBox="0 0 12 12"><path d="M2 6.5l2.7 2.7L10 3"/></svg></span>Timelapse footage</li>
          <li><span class="box"></span>Worship or wedding motion loops</li>
          <li><span class="box"></span>Pre-mixed DVDs and BluRay</li>
          <li><span class="box"></span>Entertainment lasers for concerts and clubs</li>
          <li><span class="box"></span>Entertainment lasers for text &amp; logo display</li>
          <li><span class="box"></span>Custom logo animation services</li>
          <li><span class="box"></span>Video software for creating video animations</li>
          <li><span class="box"></span>BrightReel partners</li>
          <li><span class="box"></span>Video software for live performance (Vjing)</li>
        </ul>
      </div>
      <div class="choice-col">
        <h3>I am Involved in or have interest in</h3>
        <ul>
          <li><span class="box blue checked"><svg viewBox="0 0 12 12"><path d="M2 6.5l2.7 2.7L10 3"/></svg></span>VJing (live performance video)</li>
          <li><span class="box blue checked"><svg viewBox="0 0 12 12"><path d="M2 6.5l2.7 2.7L10 3"/></svg></span>DJing (live performance audio-video)</li>
          <li><span class="box blue"></span>Performing in a band</li>
          <li><span class="box blue"></span>Video editing</li>
          <li><span class="box blue"></span>Corporate presentations</li>
          <li><span class="box blue"></span>Worship video services</li>
          <li><span class="box blue"></span>Lasers for entertainment &amp; branding</li>
        </ul>
      </div>
    </div>
  </section>

  <ul class="extras">
    <li><span class="box grey checked"><svg viewBox="0 0 12 12"><path d="M2 6.5l2.7 2.7L10 3"/></svg></span>Special offers from BrightReel partners</li>
    <li><span class="box grey"></span>Unsubscribe from all email lists</li>
  </ul>

  <div class="rule bottom"></div>

  <button class="submit">Submit
    <svg viewBox="0 0 24 24"><circle cx="12" cy="12" r="12" fill="#fff"/><path d="M6.5 12.5l3.8 3.8L17.5 8.5" fill="none" stroke="#e8590c" stroke-width="3" stroke-linecap="round" stroke-linejoin="round"/></svg>
  </button>

  <footer class="site-footer">
    <p>All Rights Reserved Copyright© 2013 - BrightReel</p>
    <div class="social"><span></span><span></span><span></span></div>
  </footer>
</div>
</body>
</html>
```